Design and brand an anti cellulite cream.
Brand is Vorrel
Product name - DLN Cream and Cellulite Smoother.
Have uploaded the packaging it will be in - will be either white with silver/grey printing or Black with white writing.
No logo just really clean modern font that stands out
Want something modern, clean, slick and classy. Think Morvaine/Lusto.
Want it to stand out on shelf and look amazing

Love the look of this product of the Tivra Hushful Brows -

The Vorrel could be a grey as the Tivra -
DLN Cream and Cellulite Smoother in grey as -Hushful brows
In pink - Target early and stubborn cellulite
200ml in grey
Updates

Vorrel is the brand - Renova is the product name - DLN cream & cellulite smoother is the tag line.

I don't want to see Vorrel and Renova together on the same line... I want Vorrel to stand out as the brand name and then the word Renova DLN cream and cellulite smoother explain the product and I want to see it designed on the bottle that I provided. Thanks

Reason: more time for designers to put their designers on the bottles that I uploaded and please remember that Vorrel is the brand name not Vorrel Renova - Renova DLN cream and cellulite smoother needs to be a bit smaller than the vorrel word as most of the designs have Vorrel Renova the same size and that is not what the product is called

Hi everyone, I have decided to take the word Renova out as it is looking very busy. Brans id Vorrel - this needs to stand out - Product name is DLN Cream & Cellulite Smoother

The front of  bottle also needs to include in it's lay out

Targets early and stubborn cellulite.

200ml

I have added a picture of a product from Tivra because I like the look of this product and would like to see Vorrel done in this look

Vorrel in grey as Tivra/.... DLN Cream and Cellulite Smoother in grey as Kissable Lips/ ... Target early and stubborn cellulite in pink as smoothing lip exfoliant/ 200ml in grey

Could do a similar look with the black packaging with white and another soft colour                                   

Target Market(s)

Women - tho men can use it

Industry/Entity Type

Printing

Logo Text

Vorrel DLN Cream & Cellulite Smoother

Logo styles of interest
Lettermark Logo
Requirements
Must have
• Vorrel is the brand so would like that to stand out - DLN Cream and Cellulite Smoother is the mane of the product

```html
<!DOCTYPE html>
<html lang="en">
<head>
<meta charset="utf-8">
<title>Vorrel – DLN Cream and Cellulite Smoother</title>
<link rel="stylesheet" href="https://fonts.googleapis.com/css2?family=Arimo:wght@400;700&family=Work+Sans:wght@300&display=swap">
<style>
  :root {
    --stage-dark: #000000;
    --stage-light: #ffffff;
    --bottle-white: #f1f1f3;
    --bottle-white-shade: #e4e6ea;
    --cap-white: #f3f1e6;
    --bottle-black: #17141b;
    --cap-black: #101013;
    --print-grey: #828282;
    --print-silver: #e2e2e2;
    --accent-pink: #d9579b;
    --accent-soft-pink: #e58cc0;
  }
  * { margin: 0; padding: 0; box-sizing: border-box; }
  html, body { width: 1200px; height: 1000px; overflow: hidden; }
  body { position: relative; font-family: "Arimo", Helvetica, Arial, sans-serif; }

  .stage { position: absolute; top: 0; width: 600px; height: 1000px; }
  .stage--dark { left: 0; width: 604px; background: var(--stage-dark); }
  .stage--light { left: 604px; width: 596px; background: var(--stage-light); }

  .bottle { position: absolute; }
  .bottle svg { display: block; }

  .label {
    position: absolute;
    text-align: center;
    transform: translateX(-50%);
    white-space: nowrap;
  }
  .brand {
    font-family: "Work Sans", "Arimo", sans-serif;
    font-weight: 300;
    font-size: 37px;
    letter-spacing: -0.5px;
  }
  .product {
    font-weight: 700;
    font-size: 19.5px;
    line-height: 26px;
  }
  .claim {
    font-weight: 400;
    font-size: 14.5px;
    line-height: 17.5px;
  }
  .volume {
    font-weight: 400;
    font-size: 15px;
  }

  .bottle--white .brand,
  .bottle--white .product,
  .bottle--white .volume { color: var(--print-grey); }
  .bottle--white .claim { color: var(--accent-pink); }

  .bottle--black .brand,
  .bottle--black .product,
  .bottle--black .volume { color: var(--print-silver); }
  .bottle--black .claim { color: var(--accent-soft-pink); }
</style>
</head>
<body>
  <div class="stage stage--dark"></div>
  <div class="stage stage--light"></div>

  <!-- White bottle with grey print -->
  <div class="bottle bottle--white" style="left:0;top:0;width:604px;height:1000px;">
    <svg width="604" height="1000" viewBox="0 0 604 1000" aria-hidden="true">
      <defs>
        <linearGradient id="white-body" x1="0" y1="0" x2="0" y2="1">
          <stop offset="0" stop-color="#efeaf2"/>
          <stop offset="0.55" stop-color="var(--bottle-white-shade)"/>
          <stop offset="1" stop-color="#f3f3ef"/>
        </linearGradient>
      </defs>
      <path class="bottle-body" fill="url(#white-body)"
        d="M268 122 H370 Q428 122 430 185 L432 470 Q440 560 444 640 Q446 730 410 758 H230 Q196 730 198 640 Q202 560 208 470 L206 185 Q208 122 268 122 Z"/>
      <path class="bottle-cap" fill="var(--cap-white)"
        d="M238 762 H400 L404 888 Q402 892 396 892 H244 Q236 892 236 886 Z"/>
    </svg>
    <div class="label brand" style="left:310px;top:318px;">Vorrel</div>
    <div class="label product" style="left:315px;top:411px;">DLN Cream<br>and<br>Cellulite Smoother</div>
    <div class="label claim" style="left:315px;top:545px;">Targets early and<br>stubborn<br>cellulite</div>
    <div class="label volume" style="left:315px;top:619px;">200ml</div>
  </div>

  <!-- Black bottle with white print -->
  <div class="bottle bottle--black" style="left:0;top:0;width:1200px;height:1000px;">
    <svg width="1200" height="1000" viewBox="0 0 1200 1000" aria-hidden="true">
      <path class="bottle-body" fill="var(--bottle-black)"
        d="M845 118 H960 Q1000 118 1004 180 L1008 470 Q1022 560 1028 640 Q1030 730 990 762 H816 Q776 730 778 640 Q782 560 796 470 L800 180 Q804 118 845 118 Z"/>
      <path class="bottle-cap" fill="var(--cap-black)"
        d="M826 764 H978 L982 866 Q980 872 972 872 H834 Q826 872 824 866 Z"/>
    </svg>
    <div class="label brand" style="left:899px;top:316px;">Vorrel</div>
    <div class="label product" style="left:903px;top:401px;">DLN Cream<br>and<br>Cellulite Smoother</div>
    <div class="label claim" style="left:904px;top:525px;">Targets early and<br>stubborn<br>cellulite</div>
    <div class="label volume" style="left:904px;top:592px;">200ml</div>
  </div>
</body>
</html>
```